Business Card Design Project

We need a logo design for a new company based in Southern California called "Norvale Security Services, Inc." We install security and camera systems for homeowners and business, to protect their assets.
Updates

Project Deadline Extended
Reason: LOGO Design completes in eight days. Would like that design decided before we finish the business cards. Thanks...

Target Market(s)

Homeowners and business owners looking for additional protection of their assets.

Industry/Entity Type

Security

Font styles to use
Serif

Requirements
Must have
• Company Name
Office# 555-472-3615
Service# 555-472-3616
email: NorvaleSecurity@brimwell.net
address: 48620 Thorncrest Lane Alder Vista, OR 91704
Nice to have
• Serving Southern California

```html
<!DOCTYPE html>
<html lang="en">
<head>
<meta charset="utf-8">
<title>Norvale Security Services, Inc. — Business Card</title>
<link rel="stylesheet" href="https://fonts.googleapis.com/css2?family=Michroma&family=Arimo:wght@400;700&display=swap">
<style>
  :root {
    --stage: #1b1b1c;
    --card-front: #2c2c2e;
    --card-back: #121418;
    --card-back-glow: #262b31;
    --accent-blue: #22486b;
    --mark-grey-light: #c9c9c9;
    --mark-grey-dark: #6e6e70;
    --text-name: #c4c4c4;
    --text-contact: #e2e2e2;
    --text-muted: #b3b3b3;
    --rule: #2a2f36;
  }
  * { box-sizing: border-box; margin: 0; padding: 0; }
  html, body { width: 1200px; height: 1134px; overflow: hidden; background: var(--stage); }
  .canvas {
    position: relative; width: 1200px; height: 1134px;
    display: flex; flex-direction: column; align-items: center; justify-content: center; gap: 60px;
  }
  .card {
    position: relative; width: 700px; height: 400px; overflow: hidden;
    box-shadow: 0 18px 40px rgba(0,0,0,.55);
  }

  /* Front side */
  .card--front { background: var(--card-front); }
  .card--front .accent-bar { position: absolute; background: var(--accent-blue); height: 16px; width: 170px; }
  .card--front .accent-bar--top { top: 0; left: 70px; }
  .card--front .accent-bar--bottom { bottom: 0; right: 70px; }
  .card--front .brand {
    position: absolute; inset: 0;
    display: flex; flex-direction: column; align-items: center; justify-content: center; gap: 34px;
  }
  .brand-square {
    width: 120px; height: 120px;
    background: linear-gradient(135deg, var(--mark-grey-light), var(--mark-grey-dark));
  }
  .brand-name {
    font-family: "Michroma", sans-serif; font-variant: small-caps;
    color: var(--text-name); letter-spacing: .08em; font-size: 22px; white-space: nowrap;
  }

  /* Back side */
  .card--back {
    background: radial-gradient(ellipse at 30% 40%, var(--card-back-glow), var(--card-back) 70%);
  }
  .card--back .accent-stripe {
    position: absolute; left: 0; right: 0; bottom: 22px; height: 8px; background: var(--accent-blue);
  }
  .card--back .brand {
    position: absolute; left: 0; top: 0; width: 330px; height: 370px;
    display: flex; flex-direction: column; align-items: center; justify-content: center; gap: 26px;
  }
  .card--back .brand-square {
    width: 96px; height: 96px; background: var(--accent-blue);
  }
  .card--back .brand-name { font-size: 13px; color: var(--text-muted); }
  .card--back .divider {
    position: absolute; left: 330px; top: 40px; bottom: 60px; width: 1px; background: var(--rule);
  }
  .contact-list {
    position: absolute; left: 370px; top: 80px; list-style: none;
    font-family: "Arimo", sans-serif; color: var(--text-contact); font-size: 17px;
    display: flex; flex-direction: column; gap: 14px;
  }
  .contact-item { display: flex; align-items: flex-start; gap: 14px; line-height: 1.35; }
  .contact-item svg { flex: none; width: 18px; height: 18px; margin-top: 2px; fill: var(--text-contact); }
  .contact-label { font-size: 12px; color: var(--text-muted); }
</style>
</head>
<body>
<main class="canvas">

  <section class="card card--front" aria-label="Business card front">
    <div class="accent-bar accent-bar--top"></div>
    <div class="accent-bar accent-bar--bottom"></div>
    <div class="brand">
      <div class="brand-square"></div>
      <p class="brand-name">Norvale Security Services, Inc</p>
    </div>
  </section>

  <section class="card card--back" aria-label="Business card back">
    <div class="brand">
      <div class="brand-square"></div>
      <p class="brand-name">Norvale Security Services, Inc</p>
    </div>
    <div class="divider"></div>
    <ul class="contact-list">
      <li class="contact-item">
        <svg viewBox="0 0 24 24" aria-hidden="true"><path d="M6.6 10.8a15.5 15.5 0 0 0 6.6 6.6l2.2-2.2c.3-.3.7-.4 1-.2 1.1.4 2.3.6 3.6.6.6 0 1 .4 1 1V20c0 .6-.4 1-1 1A17 17 0 0 1 3 4c0-.6.4-1 1-1h3.5c.6 0 1 .4 1 1 0 1.3.2 2.5.6 3.6.1.3 0 .7-.2 1z"/></svg>
        <span>555-472-3615 <span class="contact-label">(office)</span></span>
      </li>
      <li class="contact-item">
        <svg viewBox="0 0 24 24" aria-hidden="true"><path d="M6.6 10.8a15.5 15.5 0 0 0 6.6 6.6l2.2-2.2c.3-.3.7-.4 1-.2 1.1.4 2.3.6 3.6.6.6 0 1 .4 1 1V20c0 .6-.4 1-1 1A17 17 0 0 1 3 4c0-.6.4-1 1-1h3.5c.6 0 1 .4 1 1 0 1.3.2 2.5.6 3.6.1.3 0 .7-.2 1z"/></svg>
        <span>555-472-3616 <span class="contact-label">(Service)</span></span>
      </li>
      <li class="contact-item">
        <svg viewBox="0 0 24 24" aria-hidden="true"><path d="M2 5h20v14H2z M3.5 6.5 12 13l8.5-6.5" fill="none" stroke="#e2e2e2" stroke-width="1.8"/></svg>
        <span>NorvaleSecurity@brimwell.net</span>
      </li>
      <li class="contact-item">
        <svg viewBox="0 0 24 24" aria-hidden="true"><path d="M12 2a7 7 0 0 0-7 7c0 5 7 13 7 13s7-8 7-13a7 7 0 0 0-7-7zm0 9.5a2.5 2.5 0 1 1 0-5 2.5 2.5 0 0 1 0 5z"/></svg>
        <span>48620 Thorncrest Lane Alder<br>Vista, OR 91704</span>
      </li>
    </ul>
    <div class="accent-stripe"></div>
  </section>

</main>
</body>
</html>
```